Business Card Design

We like to use greens as you will see in our logo (but not TOO much green). We are a Dental Clinic in a somewhat eccentric community. We do not like the dated sharp designs which we see many dentists use. We're looking for something bright and fresh while still maintaining the integrity of the profession. Elegance is not necessarily what we are going for... we need for the design to be "mature" but also up-lifting.

See our logo.
Updates

Project Deadline Extended
Reason: We have 5 designs which we like. But we'd like to see a few more before committing to a design.

Project Deadline Extended
Reason: We are awaiting revisions to this project. We are still welcoming designs while we wait to see if designers are able to provide to us the revisions we require in order to proceed with a selection.

Target Market(s)

Younger families - ages late 20's to early 40's

Industry/Entity Type

Business

Contact Information for Business Card

Marlow T. Venn DDS 2737 S. Fennimore Ave. Ste. 8 Royal Oak, MI 48059 (248)555-0174 FX (248)555-0189 info@BrightwaveDentalMi.example BrigthwaveDentalMi.example on the back of the card we need an appointment reminder (For____ Date___ Time____) with "If you are unable to keep your appointment, kindly give 48 hours notice" at the bottom. No use of teeth in the design. DOUBLE SIDED DESIGN

Requirements
Should not have
• The use of pictures of teeth

```html
<!DOCTYPE html>
<html lang="en">
<head>
<meta charset="utf-8">
<title>Brightwave Dental Care — Business Card</title>
<link href="https://fonts.googleapis.com/css2?family=Cinzel:wght@700&family=Roboto+Condensed:wght@500;700&family=Marcellus&display=swap" rel="stylesheet">
<style>
  :root {
    --backdrop: #2b2b2b;
    --card-white: #fbfbfb;
    --card-grey: #ececec;
    --lime-pale: #e4ecaa;
    --lime: #a6cf45;
    --leaf: #78bb30;
    --leaf-deep: #62ac25;
    --forest: #1d6b37;
    --ink: #1b1b1b;
    --text-grey: #3c3c3c;
    --white: #ffffff;
  }
  * { margin: 0; padding: 0; box-sizing: border-box; }
  html, body { width: 1000px; height: 1200px; overflow: hidden; }
  body {
    background: var(--backdrop);
    position: relative;
    font-family: "Roboto Condensed", Arial, sans-serif;
  }
  .card {
    position: absolute;
    width: 723px;
    height: 423px;
    overflow: hidden;
  }
  .card--front { left: 145px; top: 72px; }
  .card--back { left: 139px; top: 637px; }

  .card__surface { position: absolute; inset: 0; }
  .card--front .card__surface {
    background: linear-gradient(90deg,
      var(--card-white) 0%, var(--card-grey) 30%, var(--lime-pale) 48%,
      var(--lime) 66%, var(--leaf) 85%, var(--leaf-deep) 100%);
  }
  .card--back .card__surface {
    background: linear-gradient(160deg, var(--card-white) 0%, var(--card-grey) 55%, var(--card-white) 100%);
  }

  .brand {
    position: absolute;
    display: flex;
    align-items: center;
    gap: 12px;
    font-family: "Marcellus", Georgia, serif;
    font-weight: 400;
    color: var(--forest);
    line-height: 1.05;
  }
  .brand__dot {
    width: 36px; height: 36px; border-radius: 50%;
    background: var(--leaf); flex: none;
  }
  .brand__name { font-size: 46px; }
  .brand__name span { display: block; font-size: 30px; letter-spacing: 1px; }
  .card--front .brand { left: 30px; top: 158px; }
  .card--back .brand { left: 50%; top: 78px; transform: translateX(-50%); }

  .holder {
    position: absolute; right: 36px; top: 86px; text-align: right;
    font-family: "Cinzel", Georgia, serif; font-weight: 700;
  }
  .holder__name { font-size: 27px; color: var(--ink); line-height: 1.1; }
  .holder__title { font-size: 21px; color: var(--white); line-height: 1.2; }

  .contacts { position: absolute; right: 36px; top: 176px; list-style: none; }
  .contacts li {
    display: flex; justify-content: flex-end; align-items: center; gap: 10px;
    font-weight: 700; font-size: 17px; color: var(--ink); height: 28px;
  }
  .contacts li + li { margin-top: 11px; }
  .contacts li.gap { margin-top: 22px; }
  .icon {
    width: 26px; height: 26px; border-radius: 50%; background: var(--white);
    display: flex; align-items: center; justify-content: center; flex: none;
  }
  .icon svg { width: 16px; height: 16px; fill: var(--leaf-deep); }

  .reminder {
    position: absolute; top: 208px; left: 0; right: 0; text-align: center;
    font-weight: 700; font-size: 17px; color: var(--ink);
  }
  .blank { display: inline-block; border-bottom: 1px solid var(--ink); height: 16px; }
  .notice {
    position: absolute; top: 260px; left: 0; right: 0; text-align: center;
    font-family: "Cinzel", Georgia, serif; font-weight: 700;
    font-size: 25px; line-height: 28px; color: var(--forest);
  }
  .address {
    position: absolute; top: 334px; left: 0; right: 0;
    display: flex; justify-content: center; align-items: center; gap: 8px;
    font-weight: 700; font-size: 17px; color: var(--text-grey);
  }
  .address .icon { background: var(--forest); }
  .address .icon svg { fill: var(--white); }
</style>
</head>
<body>

<section class="card card--front" aria-label="Business card front">
  <div class="card__surface" role="img" aria-label="Soft faceted polygon texture fading from white to fresh green"></div>

  <div class="brand">
    <div class="brand__dot"></div>
    <div class="brand__name">Brightwave<span>DENTAL CARE</span></div>
  </div>

  <div class="holder">
    <p class="holder__name">Marlow T. Venn</p>
    <p class="holder__title">DDS</p>
  </div>

  <ul class="contacts">
    <li>(555)555-0174
      <span class="icon"><svg viewBox="0 0 24 24"><path d="M6.6 10.8a15.2 15.2 0 0 0 6.6 6.6l2.2-2.2a1 1 0 0 1 1-.25 11.4 11.4 0 0 0 3.6.57 1 1 0 0 1 1 1V20a1 1 0 0 1-1 1A17 17 0 0 1 3 4a1 1 0 0 1 1-1h3.5a1 1 0 0 1 1 1c0 1.25.2 2.45.57 3.57a1 1 0 0 1-.25 1z"/></svg></span>
    </li>
    <li>(555)555-0189
      <span class="icon"><svg viewBox="0 0 24 24"><path d="M6 3h12v5H6zM4 9h16a2 2 0 0 1 2 2v6h-4v4H6v-4H2v-6a2 2 0 0 1 2-2zm4 6v4h8v-4z"/></svg></span>
    </li>
    <li class="gap">info@BrightwaveDentalMi.example
      <span class="icon"><svg viewBox="0 0 24 24"><path d="M3 5h18a1 1 0 0 1 1 1v12a1 1 0 0 1-1 1H3a1 1 0 0 1-1-1V6a1 1 0 0 1 1-1zm1 2v.4l8 5 8-5V7l-8 5z"/></svg></span>
    </li>
    <li>BrigthwaveDentalMi.example
      <span class="icon"><svg viewBox="0 0 24 24"><path d="M12 2a10 10 0 1 0 0 20 10 10 0 0 0 0-20zm0 2c.9 0 2.3 2.2 2.7 7H9.3C9.7 6.2 11.1 4 12 4zM4.1 11a8 8 0 0 1 5-6.4A15 15 0 0 0 7.3 11zm0 2h3.2a15 15 0 0 0 1.8 6.4 8 8 0 0 1-5-6.4zm5.2 0h5.4c-.4 4.8-1.8 7-2.7 7s-2.3-2.2-2.7-7zm7.4 0h3.2a8 8 0 0 1-5 6.4 15 15 0 0 0 1.8-6.4zm0-2a15 15 0 0 0-1.8-6.4 8 8 0 0 1 5 6.4z"/></svg></span>
    </li>
  </ul>
</section>

<section class="card card--back" aria-label="Business card back">
  <div class="card__surface" role="img" aria-label="Soft faceted polygon texture in white and light grey"></div>

  <div class="brand">
    <div class="brand__dot"></div>
    <div class="brand__name">Brightwave<span>DENTAL CARE</span></div>
  </div>

  <p class="reminder">(For<span class="blank" style="width:170px"></span> Date:<span class="blank" style="width:135px"></span> Time:<span class="blank" style="width:85px"></span>)</p>

  <p class="notice">If you are unable to keep your appointment,<br>kindly give 48 hours notice</p>

  <p class="address">
    <span class="icon"><svg viewBox="0 0 24 24"><path d="M12 2a7 7 0 0 0-7 7c0 5 7 13 7 13s7-8 7-13a7 7 0 0 0-7-7zm0 9.5A2.5 2.5 0 1 1 12 6.5a2.5 2.5 0 0 1 0 5z"/></svg></span>
    2737 S. Fennimore Ave. Ste. 8 Fernhollow, OR 48059
  </p>
</section>

</body>
</html>
```